Life and business Coaching Business Card and Logo

A new design for new company. We coach people to get the best out of themselves in business, life, health , family, career, relationships.
we work in Professional, executive, business and corporate environment. We use art and the processes of making art to work with getting people to delve into and change their mind maps or the way they are currently thinking so that they can move forward towards their goals strategically.
Updates

Project Deadline Extended
Reason: I have been laid up in bed with back problems and have just been able to get back to view designs. several are quiet good and I have given feedback today. I also want to take my project off refundable status as I will choose a design from this brief. regards Rosalind

Target Market(s)

Professional artistic and bold energetic individuals

Industry/Entity Type

Health

Contact Information for Business Card

Hue4Mentoring, Rosalind Pettigrew, Shaping Days Boldly,
Mob:0412958176, Ph: +61 8 93627580,
Professional, Executive, Business and Corporate Coach

Requirements
Must have
• a logo that can be used on all promotional and stationary material.
Should contain a person and be bold/colourful, simple and artistic.
Nice to have
• Room to place qualifications of Business

```html
<!DOCTYPE html>
<html lang="en">
<head>
<meta charset="utf-8">
<title>Hue4Mentoring Business Card</title>
<link rel="stylesheet" href="https://fonts.googleapis.com/css2?family=Righteous&display=swap">
<style>
  :root {
    --page-bg: #f2f2f2;
    --card-green: #1c4a3a;
    --band-teal: #2f7a78;
    --band-teal-light: #3d8c88;
    --side-olive: #3a5a2a;
    --text-white: #ffffff;
  }
  * { margin: 0; padding: 0; box-sizing: border-box; }
  html, body {
    width: 1200px; height: 797px; overflow: hidden;
    background: var(--page-bg);
    font-family: "Righteous", sans-serif;
  }
  .card {
    position: absolute; left: 100px; top: 90px;
    width: 1000px; height: 616px;
    background: var(--card-green);
    overflow: hidden;
    box-shadow: 0 10px 30px rgba(0,0,0,0.25);
  }
  .card-shapes { position: absolute; inset: 0; }
  .contact {
    position: absolute; left: 32px; top: 104px;
    color: var(--text-white);
    font-size: 16px; line-height: 29px;
    text-transform: uppercase; letter-spacing: 0.5px;
  }
  .brand {
    position: absolute; left: 195px; width: 600px; top: 340px;
    text-align: center;
    color: var(--text-white);
    text-transform: uppercase;
  }
  .brand-name { font-size: 36px; letter-spacing: 1px; }
  .brand-tagline { margin-top: 6px; font-size: 17px; letter-spacing: 1px; }
  .services {
    position: absolute; top: 574px; left: 0; width: 1000px; height: 30px;
    color: var(--text-white); font-size: 15px;
    text-transform: uppercase; letter-spacing: 0.5px;
  }
  .service {
    position: absolute; top: 4px;
    display: flex; align-items: center; gap: 10px;
  }
  .service::before {
    content: ""; width: 11px; height: 11px;
    background: var(--text-white);
    box-shadow: 0 0 6px var(--text-white);
  }
</style>
</head>
<body>
  <div class="card">
    <svg class="card-shapes" width="1000" height="616" viewBox="0 0 1000 616">
      <defs>
        <radialGradient id="centreGlow" cx="50%" cy="50%" r="50%">
          <stop offset="0%" stop-color="#0b1a14"/>
          <stop offset="55%" stop-color="#12291f"/>
          <stop offset="100%" stop-color="#1c4a3a"/>
        </radialGradient>
      </defs>
      <rect width="1000" height="616" fill="var(--card-green)" role="img" aria-label="dark green hexagon mesh texture"/>
      <ellipse cx="495" cy="250" rx="300" ry="240" fill="url(#centreGlow)"/>
      <rect x="894" y="52" width="106" height="508" fill="var(--side-olive)"/>
      <path d="M0 0 H1000 V52 H930 L905 72 H300 L270 52 H0 Z" fill="var(--band-teal)"/>
      <path d="M0 92 H260 L290 117 V262 H0 Z" fill="var(--band-teal-light)"/>
      <path d="M754 150 L894 106 V560 H754 Z" fill="var(--band-teal)"/>
      <g stroke="var(--card-green)" stroke-width="7">
        <line x1="754" y1="230" x2="894" y2="130"/>
        <line x1="754" y1="280" x2="894" y2="180"/>
        <line x1="754" y1="330" x2="894" y2="230"/>
        <line x1="754" y1="380" x2="894" y2="280"/>
        <line x1="754" y1="430" x2="894" y2="330"/>
        <line x1="754" y1="480" x2="894" y2="380"/>
        <line x1="754" y1="530" x2="894" y2="430"/>
        <line x1="790" y1="560" x2="894" y2="480"/>
      </g>
      <path d="M0 520 H250 L280 560 H1000 V616 H0 Z" fill="var(--band-teal)"/>
    </svg>

    <div class="contact">
      <p>Hue4Mentoring</p>
      <p>Rosalind Pettigrew</p>
      <p>Shaping Days Boldly</p>
      <p>Mob: 0412958176</p>
      <p>Ph: +61 8 93627580</p>
    </div>

    <div class="brand">
      <p class="brand-name">Hue4Mentoring</p>
      <p class="brand-tagline">Shaping Days Boldly</p>
    </div>

    <div class="services">
      <span class="service" style="left:183px">Professional</span>
      <span class="service" style="left:394px">Executive</span>
      <span class="service" style="left:571px">Business</span>
      <span class="service" style="left:722px">Corporate Coach</span>
    </div>
  </div>
</body>
</html>
```